Tremora - 'Destination Metasearch'

We want to make travel research and booking simple and easy within one product by enabling our users to compare destinations.

As such, we are looking for web designers to create mockups of what this ‘destination comparison’ search page could look like. Where possible, we would like for the site to remain using tremora colours (www.tremora-example.com).

Attached is a design brief that includes:

1) Company profile
- General information about us
- Audience and markets

2) Project overview
- Problem statement
- What is the project
- Expected deliverables
- Key functionalities
- User flow

An example mockup has been attached.

Designs should be mobile-first

Industry/Entity Type

Travel

Number of Pages Required

1 page

Requirements
Must have
• It must compare a destination using data for both travel and accommodation (see mockup example) and MUST be a mobile design
Nice to have
• Inclusion of additional data points (i.e. weather)
Should not have
• It must not only consider one aspect (i.e. hotel / transport).

```html
<!DOCTYPE html>
<html lang="en">
<head>
<meta charset="utf-8">
<title>Tremora – Destination Comparison Mobile Screens</title>
<link href="https://fonts.googleapis.com/css2?family=DM+Sans:wght@400;500;700&display=swap" rel="stylesheet">
<style>
:root{
  --teal:#0b97a3;
  --ink:#1b1d1f;
  --muted:#8b9095;
  --line:#e6e8ea;
  --bg:#f2f3f4;
  --chip:#eceeef;
  --frame:#111;
}
*{box-sizing:border-box;margin:0;padding:0}
html,body{width:786px;height:1200px;overflow:hidden;background:#fff}
body{font-family:"DM Sans",Arial,sans-serif;color:var(--ink)}
.canvas{position:relative;width:786px;height:1200px;overflow:hidden;background:#fff}
svg{display:block}
.heading{position:absolute;font-weight:700;font-size:8.5px}
.notes{position:absolute;font-size:12.2px;line-height:18px;color:var(--ink)}
.notes ul{list-style:none}
.notes li{position:relative;padding-left:17px}
.notes li::before{content:"";position:absolute;left:6px;top:7px;width:4px;height:4px;border-radius:50%;background:var(--ink)}
.notes p{margin-top:12px}
.demo{position:absolute;left:572px;top:205px;width:104px;height:42px}
.demo .ic{position:absolute;left:0;top:0;width:22px;height:22px;border:1px solid var(--line);border-radius:3px;display:grid;place-items:center;box-shadow:0 1px 3px rgba(0,0,0,.08)}
.demo .ic svg{width:11px;height:11px}
.demo .txt{position:absolute;left:28px;top:4px;font-size:10.5px;color:var(--muted)}
.demo .txt b{color:var(--ink);font-weight:500}
.demo .arw{position:absolute;left:78px;top:0;width:22px;height:22px;background:var(--chip);border-radius:3px;display:grid;place-items:center}
.demo .arw svg{width:12px;height:12px;color:var(--ink)}
.demo .dur{position:absolute;left:28px;top:26px;font-size:10px;color:var(--muted)}

/* phone */
.phone{position:absolute;width:312px;height:672px;transform:scale(.5);transform-origin:0 0;border:3px solid var(--frame);border-radius:18px;overflow:hidden;background:var(--bg)}
.status{height:38px;background:#fff;display:flex;justify-content:space-between;align-items:center;padding:0 14px 0 14px;font-size:12px;font-weight:500}
.status svg{width:40px;height:10px}
.topbar{height:52px;background:#fff;display:flex;align-items:center;gap:7px;padding:0 12px;box-shadow:0 1px 0 var(--line)}
.sq{width:26px;height:26px;border-radius:4px;background:var(--teal);display:grid;place-items:center;color:#fff;flex:none}
.sq svg{width:13px;height:13px}
.sq.off{background:transparent;color:#7d8388}
.sq.off.grey svg{color:#7d8388}
.sum{flex:1;font-size:7px;line-height:1.35;color:#555;margin-left:2px}
.sum b{display:block;color:var(--ink);font-weight:700}
.feed{padding:12px 12px 0}
.card{background:#fff;border-radius:6px;padding:14px 14px;margin-bottom:8px}
.c-head{display:flex;justify-content:space-between;align-items:flex-start}
.city{color:var(--teal);font-size:10.5px;font-weight:700;letter-spacing:.1px}
.date{font-size:11.5px;margin-top:4px}
.date em{font-style:normal;color:var(--teal);font-weight:700}
.x{width:22px;height:22px;border-radius:50%;background:#c9ccce;display:grid;place-items:center;color:#fff;margin-top:4px}
.x svg{width:10px;height:10px}
.sec{display:flex;justify-content:space-between;align-items:center;border-top:1px solid var(--line);margin-top:12px;padding-top:10px;font-size:10.5px;font-weight:700}
.chev-box{width:22px;height:22px;border-radius:3px;background:var(--chip);display:grid;place-items:center}
.chev-box svg{width:12px;height:12px}
.opts{display:flex;gap:20px;margin-top:16px}
.opts.three{justify-content:space-between;gap:0}
.opt-h{display:flex;align-items:center;gap:8px;font-size:11px}
.ic{width:24px;height:24px;border:1px solid var(--line);border-radius:4px;display:grid;place-items:center;flex:none;box-shadow:0 1px 2px rgba(0,0,0,.05)}
.ic svg{width:12px;height:12px}
.from{font-size:11px;color:var(--muted);margin-top:10px}
.from b,.opt-h b{color:var(--ink);font-weight:500}
.dur{font-size:11px;color:var(--muted);margin-top:3px}
.btn-main{display:block;margin-top:12px;height:32px;border-radius:3px;background:var(--teal);color:#fff;font-size:11px;font-weight:700;text-align:center;line-height:32px;border-top:1px solid var(--line)}
.gcard .sec + .opts + .sec{margin-top:14px}
.lcard{padding:16px 14px 14px}
.pair{display:flex;justify-content:space-between;margin-top:14px}
.pair .opt-h{color:var(--muted);gap:10px}
.pair .dur{margin-left:34px;margin-top:5px}
.pair .r .dur{text-align:right;margin-left:0}
.acts{display:flex;justify-content:space-between;border-top:1px solid var(--line);margin-top:12px;padding-top:8px}
.show{width:138px;height:32px;background:var(--chip);border-radius:3px;display:flex;align-items:center;justify-content:space-between;padding:0 10px;font-size:11px;color:#555}
.show svg{width:11px;height:11px}
.cmp{width:108px;height:32px;background:var(--teal);color:#fff;border-radius:3px;font-size:11px;font-weight:700;display:grid;place-items:center}
.cancel{background:#fff;color:var(--ink);font-weight:500;position:relative;z-index:3}
.lift{position:relative;z-index:3}
.dim{position:absolute;inset:0;background:rgba(28,28,28,.84);z-index:2}
.tip-close{position:absolute;top:78px;left:0;right:0;text-align:center;color:#fff;font-size:11px;font-weight:500;z-index:3}
.tip{position:absolute;left:28px;top:296px;z-index:3;color:#fff}
.tip h3{font-size:19px;font-weight:700;display:flex;align-items:center;gap:4px}
.tip h3 svg{width:18px;height:18px}
.tip p{font-size:11px;line-height:16.5px;margin-top:4px;font-weight:500}

/* search form */
.nav{height:54px;background:#fff;display:flex;align-items:center;justify-content:space-between;padding:0 14px;box-shadow:0 1px 0 var(--line)}
.nav .burger{width:18px;height:14px;color:var(--teal)}
.nav .auth{display:flex;align-items:center;gap:10px;font-size:7px;color:var(--teal);font-weight:500}
.nav .reg{background:var(--teal);color:#fff;padding:7px 8px;border-radius:2px}
.form{padding:22px 17px 0}
.field{height:48px;background:#fff;border-radius:3px;margin-bottom:6px;display:flex;justify-content:space-between;align-items:center;padding:0 16px;box-shadow:0 1px 3px rgba(0,0,0,.06)}
.field b{display:block;font-size:12px;font-weight:500}
.field span{display:block;font-size:12px;color:var(--muted);margin-top:3px}
.field svg{width:11px;height:11px;color:var(--teal)}
.search{margin-top:32px;height:48px;border-radius:3px;background:var(--teal);color:#fff;font-weight:700;font-size:12.5px;display:grid;place-items:center}

/* choose lists */
.hdr{height:52px;background:#fff;display:flex;align-items:center;gap:10px;padding:0 12px}
.hdr .ttl{flex:1;font-size:11px;font-weight:700}
.hdr .ttl small{display:block;font-size:7px;color:var(--muted);font-weight:400;margin-bottom:2px}
.tabs{display:flex;gap:18px;padding:12px 14px 6px}
.tab{width:82px;height:48px;background:#fff;border-radius:4px;text-align:center;font-size:9px;padding-top:9px}
.tab b{display:block;font-size:12px;margin-top:5px;font-weight:500}
.tab.on{background:var(--teal);color:#fff}
.rows{padding:0 14px}
.row{background:#fff;border-radius:4px;height:100px;margin-bottom:6px;position:relative}
.logo{position:absolute;left:12px;top:28px;width:80px;height:40px;display:grid;place-items:center;font-size:11px;font-weight:500;color:var(--ink)}
.photo{position:absolute;left:4px;top:6px;width:84px;height:84px;border-radius:3px}
.warm{background:linear-gradient(135deg,#5e4632,#b99872 55%,#e4d7c3)}
.cool{background:linear-gradient(160deg,#c9d3dc,#7d8c9a 55%,#4a5866)}
.meta{position:absolute;left:101px;top:5px;right:8px}
.kind{font-size:9px;color:var(--muted)}
.leg{margin-top:4px;font-size:11px;font-weight:500;line-height:20px;border-left:1.5px dotted var(--ink);padding-left:6px;margin-left:3px}
.hname{font-size:11.5px;font-weight:500;margin-top:4px}
.hdist{font-size:10.5px;color:var(--muted);margin-top:3px}
.foot{position:absolute;left:101px;right:8px;bottom:6px;display:flex;justify-content:space-between;align-items:baseline;font-size:9px;color:var(--muted)}
.foot .price{color:var(--teal);font-size:11px;font-weight:700}
.foot .price small{font-size:8.5px;font-weight:400;color:var(--muted)}
.rate{display:flex;align-items:center;gap:3px;color:var(--ink)}
.rate svg{width:10px;height:10px;color:var(--teal)}

/* summary */
.sumcard{background:#fff;border-radius:4px;margin:0 16px 10px;padding:14px 14px 8px}
.kv{display:flex;justify-content:space-between;font-size:10.5px;margin-bottom:10px}
.kv span{color:var(--muted)}
.kv.h span{color:var(--ink);font-weight:500}
.kv .edit{color:var(--teal);text-decoration:underline}
.kv.h{margin-bottom:14px;font-weight:500}
.book{position:absolute;left:0;right:0;bottom:0;height:52px;background:#fff;display:flex;justify-content:space-between;align-items:center;padding:0 16px 0 20px}
.book .tot{font-size:10px;font-weight:500}
.book .tot small{color:var(--muted);font-size:8px;font-weight:400}
.book .tot b{display:block;color:var(--teal);font-size:11.5px;margin-top:2px}
.book .go{width:106px;height:32px;background:var(--teal);color:#fff;border-radius:3px;display:grid;place-items:center;font-size:11px;font-weight:700}

/* filter */
.fbody{position:absolute;left:0;right:0;top:90px;bottom:0;background:#fff}
.fbody > *{position:absolute}
.fbtn{height:32px;border-radius:3px;display:grid;place-items:center;font-size:10.5px}
.fbtn.out{left:13px;top:10px;width:166px;border:1px solid var(--line)}
.fbtn.on{left:193px;top:10px;width:96px;background:var(--teal);color:#fff;font-weight:700}
.ft{left:17px;font-size:12.5px;font-weight:500;width:278px;display:flex;justify-content:space-between;align-items:center}
.ft small{font-size:9px;font-weight:400;margin-left:4px;flex:1}
.ft .c{width:20px;height:20px;border-radius:50%;box-shadow:0 1px 4px rgba(0,0,0,.15);display:grid;place-items:center}
.ft .c svg{width:10px;height:10px}
.chk{left:30px;display:flex;gap:10px;font-size:12.5px}
.chk i{width:13px;height:13px;border:1.5px solid #555;border-radius:2px;margin-top:3px;display:grid;place-items:center}
.chk i.on{background:var(--teal);border-color:var(--teal)}
.chk i svg{width:9px;height:9px;color:#fff}
.chk small{display:block;color:var(--muted);font-size:10.5px;margin-top:2px}
.badge{background:var(--teal);color:#fff;font-size:8px;padding:4px 6px;border-radius:3px}
.track{left:22px;width:220px;height:2px;background:#e1e3e5}
.track i{position:absolute;top:0;height:2px;background:var(--teal)}
.knob{width:11px;height:11px;border-radius:50%;background:#fff;border:1px solid #ccc;margin-top:-5px}
</style>
</head>
<body>
<svg width="0" height="0" style="position:absolute" aria-hidden="true">
<defs>
<symbol id="i-bus" viewBox="0 0 12 12"><rect x="2" y="1" width="8" height="9" rx="1.6" fill="currentColor"/><rect x="3" y="2.4" width="6" height="3.2" fill="#fff"/><circle cx="4.1" cy="8" r=".8" fill="#fff"/><circle cx="7.9" cy="8" r=".8" fill="#fff"/><rect x="3" y="9.5" width="1.6" height="1.8" fill="currentColor"/><rect x="7.4" y="9.5" width="1.6" height="1.8" fill="currentColor"/></symbol>
<symbol id="i-train" viewBox="0 0 12 12"><path d="M3 2.6C3 1.6 4 1 6 1s3 .6 3 1.6V9H3z" fill="currentColor"/><rect x="3.8" y="3" width="4.4" height="2.6" fill="#fff"/><circle cx="4.5" cy="7.4" r=".7" fill="#fff"/><circle cx="7.5" cy="7.4" r=".7" fill="#fff"/><path d="M4 9.3 3 11.2M8 9.3l1 1.9" stroke="currentColor" stroke-width="1"/></symbol>
<symbol id="i-plane" viewBox="0 0 12 12"><path d="M6 .8c.5 0 .8.6.8 1.2V5l4.3 2.3v1.2L6.8 7.3v2.2l1.4 1v.9L6 10.8l-2.2.6v-.9l1.4-1V7.3L.9 8.5V7.3L5.2 5V2c0-.6.3-1.2.8-1.2z" fill="currentColor"/></symbol>
<symbol id="i-bld" viewBox="0 0 12 12"><rect x="2.5" y="1" width="7" height="10" fill="currentColor"/><g fill="#fff"><rect x="3.6" y="2.2" width="1.2" height="1.2"/><rect x="5.4" y="2.2" width="1.2" height="1.2"/><rect x="7.2" y="2.2" width="1.2" height="1.2"/><rect x="3.6" y="4.4" width="1.2" height="1.2"/><rect x="5.4" y="4.4" width="1.2" height="1.2"/><rect x="7.2" y="4.4" width="1.2" height="1.2"/><rect x="3.6" y="6.6" width="1.2" height="1.2"/><rect x="5.4" y="6.6" width="1.2" height="1.2"/><rect x="7.2" y="6.6" width="1.2" height="1.2"/><rect x="5.2" y="8.8" width="1.6" height="2.2"/></g></symbol>
<symbol id="i-chev" viewBox="0 0 12 12"><path d="M3 4.5 6 7.5 9 4.5" fill="none" stroke="currentColor" stroke-width="1.5" stroke-linecap="round" stroke-linejoin="round"/></symbol>
<symbol id="i-up" viewBox="0 0 12 12"><path d="M3 7.5 6 4.5 9 7.5" fill="none" stroke="currentColor" stroke-width="1.3" stroke-linecap="round"/></symbol>
<symbol id="i-right" viewBox="0 0 12 12"><path d="M4.5 3 7.5 6 4.5 9" fill="none" stroke="currentColor" stroke-width="1.3" stroke-linecap="round"/></symbol>
<symbol id="i-x" viewBox="0 0 12 12"><path d="M3 3l6 6M9 3 3 9" stroke="currentColor" stroke-width="1.6" stroke-linecap="round"/></symbol>
<symbol id="i-filter" viewBox="0 0 12 12"><path d="M1.5 3h9M1.5 6h9M1.5 9h9" stroke="currentColor" stroke-width="1"/><rect x="3" y="2" width="1.6" height="2" fill="currentColor"/><rect x="7.2" y="5" width="1.6" height="2" fill="currentColor"/><rect x="4.6" y="8" width="1.6" height="2" fill="currentColor"/></symbol>
<symbol id="i-pen" viewBox="0 0 12 12"><path d="M2 10l.5-2.4L8 2.1 9.9 4 4.4 9.5z" fill="currentColor"/></symbol>
<symbol id="i-sq" viewBox="0 0 12 12"><rect x="1.5" y="1.5" width="9" height="9" rx="2" fill="currentColor"/></symbol>
<symbol id="i-list" viewBox="0 0 12 12"><path d="M1.5 2.5h9M1.5 6h9M1.5 9.5h9" stroke="currentColor" stroke-width="1.4"/></symbol>
<symbol id="i-back" viewBox="0 0 12 12"><path d="M10 6H2.5M5.5 3 2.5 6l3 3" fill="none" stroke="currentColor" stroke-width="1.3" stroke-linecap="round" stroke-linejoin="round"/></symbol>
<symbol id="i-star" viewBox="0 0 12 12"><path d="M6 .8l1.6 3.4 3.7.4-2.8 2.5.8 3.7L6 8.9l-3.3 1.9.8-3.7L.7 4.6l3.7-.4z" fill="currentColor"/></symbol>
<symbol id="i-tick" viewBox="0 0 12 12"><path d="M2.5 6.2 5 8.6 9.6 3.6" fill="none" stroke="currentColor" stroke-width="1.8"/></symbol>
<symbol id="i-burger" viewBox="0 0 18 14"><path d="M0 1.5h18M0 7h18M0 12.5h18" stroke="currentColor" stroke-width="1.6"/></symbol>
<symbol id="i-bulb" viewBox="0 0 12 12"><circle cx="6" cy="5" r="3.2" fill="currentColor"/><rect x="4.7" y="8" width="2.6" height="2.4" rx=".5" fill="currentColor"/><path d="M6 .2v.8M1.5 1.8l.6.6M10.5 1.8l-.6.6M.5 5h.9M10.6 5h.9" stroke="currentColor" stroke-width=".8"/></symbol>
<symbol id="i-status" viewBox="0 0 40 10"><g fill="currentColor"><rect x="0" y="7" width="2" height="3" rx=".4"/><rect x="3" y="5.5" width="2" height="4.5" rx=".4"/><rect x="6" y="3.5" width="2" height="6.5" rx=".4"/><rect x="9" y="1.5" width="2" height="8.5" rx=".4"/><path d="M19.5 9.6 17.7 7.7a2.6 2.6 0 0 1 3.6 0zM15.9 5.9a5.2 5.2 0 0 1 7.2 0l-1 1a3.8 3.8 0 0 0-5.2 0zM14.1 4.1a7.8 7.8 0 0 1 10.8 0l-1 1a6.4 6.4 0 0 0-8.8 0z"/><rect x="27.5" y="1.5" width="10" height="7" rx="1.8" fill="none" stroke="currentColor" stroke-width=".9" opacity=".5"/><rect x="28.8" y="2.8" width="7.4" height="4.4" rx="1"/><rect x="38.2" y="3.8" width="1" height="2.4" rx=".4" opacity=".5"/></g></symbol>
</defs>
</svg>

<main class="canvas">
  <p class="heading" style="left:254px;top:15px;font-size:8.5px">Revised - 28 February 2022</p>
  <p class="heading" style="left:63px;top:36px">UI Mobile View - Grid</p>
  <p class="heading" style="left:425px;top:36px">UI Mobile View - List</p>

  <div class="notes" style="left:199px;top:57px">
    <p style="margin:0">Revised Grid :</p>
    <ul>
      <li>Remove buttons on top</li>
      <li>Show Details could just be a<br>mini arrow</li>
      <li>Add Compare Button</li>
    </ul>
  </div>

  <div class="notes" style="left:559px;top:57px;width:222px">
    <p style="margin:0">Revised List :</p>
    <ul>
      <li>Remove buttons on top</li>
      <li>Include the ‘Duration of transport’</li>
    </ul>
    <p>*Cannot apply the same Show Details Button like on Grid because if the price have more than 3 digit it will collide with Mini Arrow Button</p>
  </div>

  <div class="demo">
    <span class="ic"><svg><use href="#i-bld"/></svg></span>
    <span class="txt">From <b>$1.404</b></span>
    <span class="arw"><svg><use href="#i-chev"/></svg></span>
    <span class="dur">12h 15m</span>
  </div>

  <div class="notes" style="left:559px;top:277px;width:222px">
    <p style="margin:0">Whole Card is clickable, the function is to ‘Select Destination’. Exactly like the current Tremora’s product.</p>
  </div>

  <!-- Grid view, row 1 -->
  <section class="phone" style="left:29px;top:54px">
    <div class="status"><span>19:41</span><svg><use href="#i-status"/></svg></div>
    <div class="topbar">
      <span class="sq"><svg><use href="#i-filter"/></svg></span>
      <p class="sum">Hamburg, 17-21 Feb | 2 Adults, 1 Child<b>Munich, Madrid, Berlin, Jakarta, Ne..</b></p>
      <span class="sq"><svg><use href="#i-pen"/></svg></span>
      <span class="sq"><svg><use href="#i-sq"/></svg></span>
      <span class="sq off"><svg><use href="#i-list"/></svg></span>
    </div>
    <div class="feed">
      <article class="card gcard">
        <div class="c-head"><div><p class="city">MUNICH, GERMANY</p><p class="date">17 - 21 Feb | from <em>$2.052,48</em></p></div><span class="x"><svg><use href="#i-x"/></svg></span></div>
        <div class="sec"><span>TRANSPORTATION</span><span class="chev-box"><svg><use href="#i-chev"/></svg></span></div>
        <div class="opts three">
          <div><div class="opt-h"><span class="ic"><svg><use href="#i-bus"/></svg></span>Bus</div><p class="from">From <b>$40</b></p><p class="dur">12h 15m</p></div>
          <div><div class="opt-h"><span class="ic"><svg><use href="#i-train"/></svg></span>Train</div><p class="from">From <b>$90</b></p><p class="dur">8h 20m</p></div>
          <div><div class="opt-h"><span class="ic"><svg><use href="#i-plane"/></svg></span>Flight</div><p class="from">From <b>$1.940</b></p><p class="dur">1h 45m</p></div>
        </div>
        <div class="sec"><span>ACCOMMODATION</span><span class="chev-box"><svg><use href="#i-chev"/></svg></span></div>
        <div class="opts">
          <div><div class="opt-h"><span class="ic"><svg><use href="#i-bus"/></svg></span>Hotel</div><p class="from">From <b>$40</b></p><p class="dur">3 Days 2 Night</p></div>
          <div><div class="opt-h"><span class="ic"><svg><use href="#i-bld"/></svg></span>Apartment</div><p class="from">From <b>$90</b></p><p class="dur">3 Days 2 Night</p></div>
        </div>
        <span class="btn-main">Select to Compare</span>
      </article>
      <article class="card gcard">
        <div class="c-head"><div><p class="city">MADRID, SPAIN</p><p class="date">17 - 21 Feb | from <em>$2.052,48</em></p></div><span class="x"><svg><use href="#i-x"/></svg></span></div>
        <div class="sec"><span>TRANSPORTATION</span><span class="chev-box"><svg><use href="#i-chev"/></svg></span></div>
        <div class="opts three">
          <div><div class="opt-h"><span class="ic"><svg><use href="#i-bus"/></svg></span>Bus</div><p class="from">From <b>$40</b></p><p class="dur">12h 15m</p></div>
          <div><div class="opt-h"><span class="ic"><svg><use href="#i-train"/></svg></span>Train</div><p class="from">From <b>$90</b></p><p class="dur">8h 20m</p></div>
          <div><div class="opt-h"><span class="ic"><svg><use href="#i-plane"/></svg></span>Flight</div><p class="from">From <b>$160</b></p><p class="dur">1h 45m</p></div>
        </div>
        <div class="sec"><span>ACCOMMODATION</span><span class="chev-box"><svg><use href="#i-chev"/></svg></span></div>
      </article>
    </div>
  </section>

  <!-- List view, row 1 -->
  <section class="phone" style="left:389px;top:54px">
    <div class="status"><span>19:41</span><svg><use href="#i-status"/></svg></div>
    <div class="topbar">
      <span class="sq"><svg><use href="#i-filter"/></svg></span>
      <p class="sum">Hamburg, 17-21 Feb | 2 Adults, 1 Child<b>Munich, Madrid, Berlin, Jakarta, Ne..</b></p>
      <span class="sq"><svg><use href="#i-pen"/></svg></span>
      <span class="sq off"><svg><use href="#i-sq"/></svg></span>
      <span class="sq"><svg><use href="#i-list"/></svg></span>
    </div>
    <div class="feed">
      <article class="card lcard">
        <div class="c-head"><div><p class="city">MUNICH, GERMANY</p><p class="date">17 - 21 Feb | from <em>$2.052,48</em></p></div><span class="x"><svg><use href="#i-x"/></svg></span></div>
        <div class="pair"><div><div class="opt-h"><span class="ic"><svg><use href="#i-bus"/></svg></span>From <b>$40</b></div><p class="dur">12h 15m</p></div><div class="r"><div class="opt-h"><span class="ic"><svg><use href="#i-bld"/></svg></span>From <b>$1.304</b></div><p class="dur">3 Days 2 Night</p></div></div>
        <div class="acts"><span class="show">Show Details<svg><use href="#i-chev"/></svg></span><span class="cmp">Compare</span></div>
      </article>
      <article class="card lcard">
        <div class="c-head"><div><p class="city">MADRID, SPAIN</p><p class="date">17 - 21 Feb | from <em>$2.052,48</em></p></div><span class="x"><svg><use href="#i-x"/></svg></span></div>
        <div class="pair"><div><div class="opt-h"><span class="ic"><svg><use href="#i-bus"/></svg></span>From <b>$40</b></div><p class="dur">12h 15m</p></div><div class="r"><div class="opt-h"><span class="ic"><svg><use href="#i-bld"/></svg></span>From <b>$90</b></div><p class="dur">3 Days 2 Night</p></div></div>
        <div class="acts"><span class="show">Show Details<svg><use href="#i-chev"/></svg></span><span class="cmp">Compare</span></div>
      </article>
      <article class="card lcard">
        <div class="c-head"><div><p class="city">BERLIN, GERMANY</p><p class="date">17 - 21 Feb | from <em>$2.052,48</em></p></div><span class="x"><svg><use href="#i-x"/></svg></span></div>
        <div class="pair"><div><div class="opt-h"><span class="ic"><svg><use href="#i-bus"/></svg></span>From <b>$40</b></div><p class="dur">12h 15m</p></div><div class="r"><div class="opt-h"><span class="ic"><svg><use href="#i-bld"/></svg></span>From <b>$90</b></div><p class="dur">3 Days 2 Night</p></div></div>
        <div class="acts"><span class="show">Show Details<svg><use href="#i-chev"/></svg></span><span class="cmp">Compare</span></div>
      </article>
      <article class="card lcard">
        <div class="c-head"><div><p class="city">JAKARTA, INDONESIA</p><p class="date">17 - 21 Feb | from <em>$2.052,48</em></p></div><span class="x"><svg><use href="#i-x"/></svg></span></div>
      </article>
    </div>
  </section>

  <!-- Search form, row 2 -->
  <section class="phone" style="left:29px;top:424px">
    <div class="status"><span style="padding-left:10px">9:41</span><svg><use href="#i-status"/></svg></div>
    <div class="nav"><svg class="burger"><use href="#i-burger"/></svg><div class="auth"><span>Sign In</span><span class="reg">Register</span></div></div>
    <div class="form">
      <div class="field"><div><b>Departure City</b><span>Hamburg</span></div><svg><use href="#i-chev"/></svg></div>
      <div class="field"><div><b>Departure Date</b><span>Thursday, 17 Feb 2022</span></div><svg><use href="#i-chev"/></svg></div>
      <div class="field"><div><b>Return Date</b><span>Monday, 21 Feb 2022</span></div><svg><use href="#i-chev"/></svg></div>
      <div class="field"><div><b>People</b><span>2 Adults, 1 Child</span></div><svg><use href="#i-chev"/></svg></div>
      <div class="field"><div><b>Destination City</b><span>3 Selected</span></div><svg><use href="#i-chev"/></svg></div>
      <div class="field"><div><b>Trip</b><span>Round Trip</span></div><svg><use href="#i-chev"/></svg></div>
      <div class="search">Search</div>
    </div>
  </section>

  <!-- Compare tip overlay, row 2 -->
  <section class="phone" style="left:218px;top:424px">
    <div class="status"><span>19:41</span><svg><use href="#i-status"/></svg></div>
    <div class="topbar">
      <span class="sq"><svg><use href="#i-filter"/></svg></span>
      <p class="sum">Hamburg, 17-21 Feb | 2 Adults, 1 Child<b>Munich, Madrid, Berlin, Jakarta, Ne..</b></p>
      <span class="sq"><svg><use href="#i-pen"/></svg></span>
      <span class="sq off"><svg><use href="#i-sq"/></svg></span>
      <span class="sq"><svg><use href="#i-list"/></svg></span>
    </div>
    <div class="feed">
      <article class="card lcard">
        <div class="c-head"><div><p class="city">MUNICH, GERMANY</p><p class="date">17 - 21 Feb | from <em>$2.052,48</em></p></div><span class="x"><svg><use href="#i-x"/></svg></span></div>
        <div class="pair"><div><div class="opt-h"><span class="ic"><svg><use href="#i-bus"/></svg></span>From <b>$40</b></div><p class="dur">12h 15m</p></div><div class="r"><div class="opt-h"><span class="ic"><svg><use href="#i-bld"/></svg></span>From <b>$1.304</b></div><p class="dur">3 Days 2 Night</p></div></div>
        <div class="acts"><span class="show">Show Details<svg><use href="#i-chev"/></svg></span><span class="cmp cancel">Cancel Compare</span></div>
      </article>
      <article class="card lcard">
        <div class="c-head"><div><p class="city">MADRID, SPAIN</p><p class="date">17 - 21 Feb | from <em>$2.052,48</em></p></div><span class="x"><svg><use href="#i-x"/></svg></span></div>
        <div class="pair"><div><div class="opt-h"><span class="ic"><svg><use href="#i-bus"/></svg></span>From <b>$40</b></div><p class="dur">12h 15m</p></div><div class="r"><div class="opt-h"><span class="ic"><svg><use href="#i-bld"/></svg></span>From <b>$90</b></div><p class="dur">3 Days 2 Night</p></div></div>
        <div class="acts"><span class="show">Show Details<svg><use href="#i-chev"/></svg></span><span class="cmp cancel">Cancel Compare</span></div>
      </article>
      <article class="card lcard">
        <div class="c-head"><div><p class="city">BERLIN, GERMANY</p><p class="date">17 - 21 Feb | from <em>$2.052,48</em></p></div><span class="x"><svg><use href="#i-x"/></svg></span></div>
        <div class="pair"><div><div class="opt-h"><span class="ic"><svg><use href="#i-bus"/></svg></span>From <b>$40</b></div><p class="dur">12h 15m</p></div><div class="r"><div class="opt-h"><span class="ic"><svg><use href="#i-bld"/></svg></span>From <b>$90</b></div><p class="dur">3 Days 2 Night</p></div></div>
        <div class="acts"><span class="show">Show Details<svg><use href="#i-chev"/></svg></span><span class="cmp lift">Compare</span></div>
      </article>
      <article class="card lcard">
        <div class="c-head"><div><p class="city">JAKARTA, INDONESIA</p><p class="date">17 - 21 Feb | from <em>$2.052,48</em></p></div><span class="x"><svg><use href="#i-x"/></svg></span></div>
      </article>
    </div>
    <div class="dim"></div>
    <p class="tip-close">Tap Anywhere to Close</p>
    <div class="tip"><h3><svg><use href="#i-bulb"/></svg>Pro Tip</h3><p>Click a ‘Compare’ button to compare<br>a destination with another<br>destination easily</p></div>
  </section>

  <!-- List view, row 2 -->
  <section class="phone" style="left:407px;top:424px">
    <div class="status"><span>19:41</span><svg><use href="#i-status"/></svg></div>
    <div class="topbar">
      <span class="sq"><svg><use href="#i-filter"/></svg></span>
      <p class="sum">Hamburg, 17-21 Feb | 2 Adults, 1 Child<b>Munich, Madrid, Berlin, Jakarta, Ne..</b></p>
      <span class="sq"><svg><use href="#i-pen"/></svg></span>
      <span class="sq off"><svg><use href="#i-sq"/></svg></span>
      <span class="sq"><svg><use href="#i-list"/></svg></span>
    </div>
    <div class="feed">
      <article class="card lcard">
        <div class="c-head"><div><p class="city">MUNICH, GERMANY</p><p class="date">17 - 21 Feb | from <em>$2.052,48</em></p></div><span class="x"><svg><use href="#i-x"/></svg></span></div>
        <div class="pair"><div><div class="opt-h"><span class="ic"><svg><use href="#i-bus"/></svg></span>From <b>$40</b></div><p class="dur">12h 15m</p></div><div class="r"><div class="opt-h"><span class="ic"><svg><use href="#i-bld"/></svg></span>From <b>$1.304</b></div><p class="dur">3 Days 2 Night</p></div></div>
        <div class="acts"><span class="show">Show Details<svg><use href="#i-chev"/></svg></span><span class="cmp">Compare</span></div>
      </article>
      <article class="card lcard">
        <div class="c-head"><div><p class="city">MADRID, SPAIN</p><p class="date">17 - 21 Feb | from <em>$2.052,48</em></p></div><span class="x"><svg><use href="#i-x"/></svg></span></div>
        <div class="pair"><div><div class="opt-h"><span class="ic"><svg><use href="#i-bus"/></svg></span>From <b>$40</b></div><p class="dur">12h 15m</p></div><div class="r"><div class="opt-h"><span class="ic"><svg><use href="#i-bld"/></svg></span>From <b>$90</b></div><p class="dur">3 Days 2 Night</p></div></div>
        <div class="acts"><span class="show">Show Details<svg><use href="#i-chev"/></svg></span><span class="cmp">Compare</span></div>
      </article>
      <article class="card lcard">
        <div class="c-head"><div><p class="city">BERLIN, GERMANY</p><p class="date">17 - 21 Feb | from <em>$2.052,48</em></p></div><span class="x"><svg><use href="#i-x"/></svg></span></div>
        <div class="pair"><div><div class="opt-h"><span class="ic"><svg><use href="#i-bus"/></svg></span>From <b>$40</b></div><p class="dur">12h 15m</p></div><div class="r"><div class="opt-h"><span class="ic"><svg><use href="#i-bld"/></svg></span>From <b>$90</b></div><p class="dur">3 Days 2 Night</p></div></div>
        <div class="acts"><span class="show">Show Details<svg><use href="#i-chev"/></svg></span><span class="cmp">Compare</span></div>
      </article>
      <article class="card lcard">
        <div class="c-head"><div><p class="city">JAKARTA, INDONESIA</p><p class="date">17 - 21 Feb | from <em>$2.052,48</em></p></div><span class="x"><svg><use href="#i-x"/></svg></span></div>
      </article>
    </div>
  </section>

  <!-- Grid view, row 2 -->
  <section class="phone" style="left:596px;top:424px">
    <div class="status"><span>19:41</span><svg><use href="#i-status"/></svg></div>
    <div class="topbar">
      <span class="sq"><svg><use href="#i-filter"/></svg></span>
      <p class="sum">Hamburg, 17-21 Feb | 2 Adults, 1 Child<b>Munich, Madrid, Berlin, Jakarta, Ne..</b></p>
      <span class="sq"><svg><use href="#i-pen"/></svg></span>
      <span class="sq"><svg><use href="#i-sq"/></svg></span>
      <span class="sq off"><svg><use href="#i-list"/></svg></span>
    </div>
    <div class="feed">
      <article class="card gcard">
        <div class="c-head"><div><p class="city">MUNICH, GERMANY</p><p class="date">17 - 21 Feb | from <em>$2.052,48</em></p></div><span class="x"><svg><use href="#i-x"/></svg></span></div>
        <div class="sec"><span>TRANSPORTATION</span><span class="chev-box"><svg><use href="#i-chev"/></svg></span></div>
        <div class="opts three">
          <div><div class="opt-h"><span class="ic"><svg><use href="#i-bus"/></svg></span>Bus</div><p class="from">From <b>$40</b></p><p class="dur">12h 15m</p></div>
          <div><div class="opt-h"><span class="ic"><svg><use href="#i-train"/></svg></span>Train</div><p class="from">From <b>$90</b></p><p class="dur">8h 20m</p></div>
          <div><div class="opt-h"><span class="ic"><svg><use href="#i-plane"/></svg></span>Flight</div><p class="from">From <b>$1.940</b></p><p class="dur">1h 45m</p></div>
        </div>
        <div class="sec"><span>ACCOMMODATION</span><span class="chev-box"><svg><use href="#i-chev"/></svg></span></div>
        <div class="opts">
          <div><div class="opt-h"><span class="ic"><svg><use href="#i-bus"/></svg></span>Hotel</div><p class="from">From <b>$40</b></p><p class="dur">3 Days 2 Night</p></div>
          <div><div class="opt-h"><span class="ic"><svg><use href="#i-bld"/></svg></span>Apartment</div><p class="from">From <b>$90</b></p><p class="dur">3 Days 2 Night</p></div>
        </div>
        <span class="btn-main">Select to Compare</span>
      </article>
      <article class="card gcard">
        <div class="c-head"><div><p class="city">MADRID, SPAIN</p><p class="date">17 - 21 Feb | from <em>$2.052,48</em></p></div><span class="x"><svg><use href="#i-x"/></svg></span></div>
        <div class="sec"><span>TRANSPORTATION</span><span class="chev-box"><svg><use href="#i-chev"/></svg></span></div>
        <div class="opts three">
          <div><div class="opt-h"><span class="ic"><svg><use href="#i-bus"/></svg></span>Bus</div><p class="from">From <b>$40</b></p><p class="dur">12h 15m</p></div>
          <div><div class="opt-h"><span class="ic"><svg><use href="#i-train"/></svg></span>Train</div><p class="from">From <b>$90</b></p><p class="dur">8h 20m</p></div>
          <div><div class="opt-h"><span class="ic"><svg><use href="#i-plane"/></svg></span>Flight</div><p class="from">From <b>$160</b></p><p class="dur">1h 45m</p></div>
        </div>
        <div class="sec"><span>ACCOMMODATION</span><span class="chev-box"><svg><use href="#i-chev"/></svg></span></div>
      </article>
    </div>
  </section>

  <!-- Flight choice, row 3 -->
  <section class="phone" style="left:29px;top:792px">
    <div class="status"><span>19:41</span><svg><use href="#i-status"/></svg></div>
    <div class="hdr">
      <span class="sq"><svg><use href="#i-back"/></svg></span>
      <p class="ttl"><small>Choose Accomodation</small>13 Hotel &amp; 4 Apartment Available</p>
      <span class="sq"><svg><use href="#i-filter"/></svg></span>
    </div>
    <div class="tabs"><div class="tab">Bus<b>$45,01</b></div><div class="tab">Train<b>$25,27</b></div><div class="tab on">Flight<b>$25,27</b></div></div>
    <div class="rows">
      <div class="row"><span class="logo">Aerovia</span><div class="meta"><p class="kind">Flight</p><p class="leg">06:00 Hamburg<br>08:20 Munich International</p></div><div class="foot"><span>Direct &nbsp; 1h 20m</span><span class="price">$45<small>/Passenger</small></span></div></div>
      <div class="row"><span class="logo">Aerovia</span><div class="meta"><p class="kind">Flight</p><p class="leg">06:00 Hamburg<br>08:20 Munich International</p></div><div class="foot"><span>Direct &nbsp; 1h 20m</span><span class="price">$45<small>/Passenger</small></span></div></div>
      <div class="row"><span class="logo">Aerovia</span><div class="meta"><p class="kind">Flight</p><p class="leg">06:00 Hamburg<br>08:20 Munich International</p></div><div class="foot"><span>Direct &nbsp; 1h 20m</span><span class="price">$45<small>/Passenger</small></span></div></div>
      <div class="row"><span class="logo">Aerovia</span><div class="meta"><p class="kind">Flight</p><p class="leg">06:00 Hamburg<br>08:20 Munich International</p></div><div class="foot"><span>Direct &nbsp; 1h 20m</span><span class="price">$45<small>/Passenger</small></span></div></div>
      <div class="row"><span class="logo">Aerovia</span><div class="meta"><p class="kind">Flight</p><p class="leg">06:00 Hamburg<br>08:20 Munich International</p></div><div class="foot"><span>Direct &nbsp; 1h 20m</span><span class="price">$45<small>/Passenger</small></span></div></div>
    </div>
  </section>

  <!-- Hotel choice, row 3 -->
  <section class="phone" style="left:218px;top:792px">
    <div class="status"><span>19:41</span><svg><use href="#i-status"/></svg></div>
    <div class="hdr">
      <span class="sq"><svg><use href="#i-back"/></svg></span>
      <p class="ttl"><small>Choose Accomodation</small>13 Hotel &amp; 4 Apartment Available</p>
      <span class="sq"><svg><use href="#i-filter"/></svg></span>
    </div>
    <div class="tabs"><div class="tab on">Hotel<b>$45,01</b></div><div class="tab">Apartment<b>$25,27</b></div></div>
    <div class="rows">
      <div class="row"><div class="photo warm" role="img" aria-label="Hotel room photo"></div><div class="meta"><p class="kind">Hotel</p><p class="hname">Linden Royal Hotel Munich</p><p class="hdist">1 km from City Center</p></div><div class="foot"><span class="price">$45<small>/Room/Night</small></span><span class="rate"><svg><use href="#i-star"/></svg>4.7 &nbsp;(160)</span></div></div>
      <div class="row"><div class="photo warm" role="img" aria-label="Hotel room photo"></div><div class="meta"><p class="kind">Hotel</p><p class="hname">Garden Court Munich</p><p class="hdist">5+ km from City Center</p></div><div class="foot"><span class="price">$45<small>/Room/Night</small></span><span class="rate"><svg><use href="#i-star"/></svg>4.7 &nbsp;(160)</span></div></div>
      <div class="row"><div class="photo cool" role="img" aria-label="Hotel building exterior photo"></div><div class="meta"><p class="kind">Hotel</p><p class="hname">Isar Inn Design</p><p class="hdist">2 km from City Center</p></div><div class="foot"><span class="price">$45<small>/Room/Night</small></span><span class="rate"><svg><use href="#i-star"/></svg>4.7 &nbsp;(160)</span></div></div>
      <div class="row"><div class="photo cool" role="img" aria-label="Hotel building exterior photo"></div><div class="meta"><p class="kind">Hotel</p><p class="hname">City Hotel</p><p class="hdist">1 km from City Center</p></div><div class="foot"><span class="price">$45<small>/Room/Night</small></span><span class="rate"><svg><use href="#i-star"/></svg>4.7 &nbsp;(160)</span></div></div>
      <div class="row"><div class="photo warm" role="img" aria-label="Hotel room photo"></div><div class="meta"><p class="kind">Hotel</p><p class="hname">Bluegate Munich</p><p class="hdist">1 km from City Center</p></div><div class="foot"><span class="price">$45<small>/Room/Night</small></span><span class="rate"><svg><use href="#i-star"/></svg>4.7 &nbsp;(160)</span></div></div>
    </div>
  </section>

  <!-- Booking summary, row 3 -->
  <section class="phone" style="left:407px;top:792px">
    <div class="status"><span>19:41</span><svg><use href="#i-status"/></svg></div>
    <div class="hdr">
      <span class="sq"><svg><use href="#i-back"/></svg></span>
      <p class="ttl"><small>Book Summary for</small>Munich, Germany</p>
    </div>
    <div style="height:14px"></div>
    <div class="sumcard">
      <div class="kv h"><span>Selected Destination</span>Munich, Germany</div>
      <div class="kv"><span>Date</span>17 - 21 Feb 2022</div>
      <div class="kv"><span>Departure City</span>Hamburg, Germany</div>
    </div>
    <div class="sumcard">
      <div class="kv h"><span>Transportation</span><em class="edit" style="font-style:normal">Edit</em></div>
      <div class="kv"><span>Name</span>Aerovia</div>
      <div class="kv"><span>Pasenggers</span>2 Adults, 1 Child</div>
      <div class="kv"><span>Seat Class</span>Economy</div>
      <div class="kv"><span>Trip</span>Direct</div>
      <div class="kv"><span>Round Trip</span>Yes</div>
      <div class="kv"><span>Total Price</span>$900.00</div>
    </div>
    <div class="sumcard">
      <div class="kv h"><span>Accomodation</span><em class="edit" style="font-style:normal">Edit</em></div>
      <div class="kv"><span>Name</span>Linden Royal Hotel Munich</div>
      <div class="kv"><span>Person</span>2 Adults, 1 Child</div>
      <div class="kv"><span>Room Type</span>Deluxe</div>
      <div class="kv"><span>Duration</span>1 Room X 3 Night</div>
      <div class="kv"><span>Total Price</span>$600</div>
    </div>
    <div class="book"><p class="tot">TOTAL PRICE <small>(incl tax)</small><b>$1.400,00</b></p><span class="go">Book</span></div>
  </section>

  <!-- Transport filter, row 3 -->
  <section class="phone" style="left:596px;top:792px">
    <div class="status"><span>19:41</span><svg><use href="#i-status"/></svg></div>
    <div class="topbar">
      <span class="sq"><svg><use href="#i-filter"/></svg></span>
      <p class="sum">Hamburg, 17-21 Feb | 2 Adults, 1 Child<b>Munich, Madrid, Berlin, Jakarta, Ne..</b></p>
      <span class="sq"><svg><use href="#i-pen"/></svg></span>
      <span class="sq"><svg><use href="#i-sq"/></svg></span>
      <span class="sq off"><svg><use href="#i-list"/></svg></span>
    </div>
    <div class="fbody">
      <span class="fbtn out">Transportation Filter</span>
      <span class="fbtn on">Apply Filter</span>
      <p class="ft" style="top:67px">Arrival Time<span class="c"><svg><use href="#i-up"/></svg></span></p>
      <div class="chk" style="top:98px"><i></i><p>00:00 - 06:00<small>Early Morning</small></p></div>
      <div class="chk" style="top:136px"><i class="on"><svg><use href="#i-tick"/></svg></i><p>06:00 - 12:00<small>Morning</small></p></div>
      <div class="chk" style="top:174px"><i></i><p>12:00 - 18:00<small>Afternoon</small></p></div>
      <div class="chk" style="top:212px"><i></i><p>18:00 - 00:00<small>Evening</small></p></div>
      <p class="ft" style="top:271px">Departure Time<span class="c"><svg><use href="#i-right"/></svg></span></p>
      <p class="ft" style="top:321px">Price</p>
      <span class="badge" style="left:32px;top:352px">€120</span>
      <span class="badge" style="left:200px;top:352px">€2300</span>
      <div class="track" style="top:382px"><i style="left:15px;width:130px"></i></div>
      <span class="knob" style="left:32px;top:382px"></span>
      <span class="knob" style="left:164px;top:382px"></span>
      <p class="ft" style="top:420px">Duration<small>(from arrival city to destination)</small></p>
      <span class="badge" style="left:60px;top:451px">1 Hour</span>
      <div class="track" style="top:481px"><i style="left:0;width:52px"></i></div>
      <span class="knob" style="left:71px;top:481px"></span>
      <p class="ft" style="top:518px">Departure Stops<span class="c"><svg><use href="#i-up"/></svg></span></p>
      <div class="chk" style="top:551px"><i></i><p>Hamburg Hbf</p></div>
    </div>
  </section>
</main>
</body>
</html>
```